political campaign lawn sign - Governor's Council in Massachuesetts

We are looking for a political lawn sign. We are running a campaign for Governor's Council in Massachusetts. This sign will be on the lawn of homes and businesses so people driving by will see it. It needs to be simple and bold. The last name is long so maybe it could say vote for Marty and then Kolbeck will be big a bold on the next line??
We need it to say:
Vote for Martin Kolbeck
Governor's Council.

Target Market(s)

local residents

Industry/Entity Type

Politcal Campaign

Font styles to use
Sans Serif
Other font styles liked:
• not sure what font but a modern looking one such as Helvetica, Arial, Sans Seri, sharp sans..

Colors
0054AA
0677BA
7BADD7
CADEEF
E8F1F8
00AB8E
00BBA5
67D7C9
C6EFE9
E9F9F6
FFF300
FFF600
FEFA6F
FFFEC7
FFFEE8

Requirements
Must have
• My name written out with a Capital D and R but lower case for every other letter so its Marty Kolbeck
Nice to have
• modern font , the Colors of the lawn sign should have Blue, Yellow and White something bold that will stand out
Should not have
• any maps of Massachusetts

```html
<!DOCTYPE html>
<html lang="en">
<head>
<meta charset="utf-8">
<title>Vote for Marty Kolbeck – Governor's Council</title>
<link href="https://fonts.googleapis.com/css2?family=Kalam:wght@400&family=Montserrat:wght@400&family=Poppins:wght@700;800&family=Russo+One&display=swap" rel="stylesheet">
<style>
  :root {
    --page: #e6e8ea;
    --sign-cream: #fdfcef;
    --blue: #0054aa;
    --blue-mid: #1a5fae;
    --yellow: #fff300;
    --black: #0b0b0b;
    --white: #ffffff;
    --teal: #00abc4;
  }
  * { margin: 0; padding: 0; box-sizing: border-box; }
  html, body {
    width: 1200px; height: 736px; overflow: hidden;
    background: var(--page);
  }
  .canvas { position: relative; width: 1200px; height: 736px; }
  .sign {
    position: absolute; left: 30px; top: 115px;
    width: 1140px; height: 505px;
    background: var(--sign-cream);
    overflow: hidden;
  }
  .sign-shapes { position: absolute; inset: 0; }
  .campaign-mark {
    position: absolute; left: 60px; top: 205px;
    display: flex; align-items: center; gap: 16px;
  }
  .campaign-mark__dot {
    width: 56px; height: 56px; border-radius: 50%;
    background: var(--teal); flex: none;
  }
  .campaign-mark__name {
    font-family: "Poppins", sans-serif; font-weight: 800;
    font-size: 34px; line-height: 1.05; color: var(--blue);
    text-transform: uppercase;
  }
  .vote-for {
    position: absolute; left: 395px; top: 60px;
    font-family: "Kalam", cursive; font-size: 62px;
    color: var(--black); line-height: 1;
  }
  .first-name {
    position: absolute; left: 680px; top: 94px;
    font-family: "Russo One", sans-serif; font-size: 72px;
    color: var(--black); line-height: 1; letter-spacing: 1px;
  }
  .stars {
    position: absolute; left: 968px; top: 104px;
    font-family: "Poppins", sans-serif; font-size: 34px;
    color: var(--black); letter-spacing: 2px; line-height: 1;
  }
  .last-name {
    position: absolute; left: 425px; top: 188px;
    font-family: "Russo One", sans-serif; font-size: 100px;
    color: var(--white); line-height: 1; letter-spacing: 4px;
  }
  .office {
    position: absolute; left: 420px; top: 305px;
    font-family: "Poppins", sans-serif; font-weight: 700;
    font-size: 60px; color: var(--blue-mid); line-height: 1;
    letter-spacing: -0.5px;
  }
  .web {
    position: absolute; left: 545px; top: 428px;
    display: flex; align-items: center; gap: 12px;
    font-family: "Montserrat", sans-serif; font-size: 38px;
    color: var(--white); letter-spacing: 5px; line-height: 1;
  }
  .web svg { width: 28px; height: 28px; flex: none; }
</style>
</head>
<body>
<div class="canvas">
  <div class="sign">
    <svg class="sign-shapes" viewBox="0 0 1140 505" width="1140" height="505" aria-hidden="true">
      <polygon points="655,84 1095,84 1095,184 612,184" fill="var(--yellow)"/>
      <polygon points="395,184 1095,184 1055,292 395,292" fill="var(--blue)"/>
      <polygon points="0,505 0,487 470,487 515,410 1100,410 1100,487 1140,487 1140,505" fill="var(--black)"/>
    </svg>

    <div class="campaign-mark">
      <span class="campaign-mark__dot"></span>
      <span class="campaign-mark__name">Council<br>Forward</span>
    </div>

    <div class="vote-for">Vote for</div>
    <div class="first-name">MARTY</div>
    <div class="stars">★★★</div>
    <div class="last-name">KOLBECK</div>
    <div class="office">Governer's Council.</div>

    <div class="web">
      <svg viewBox="0 0 24 24" fill="none" stroke="#fff" stroke-width="1.8" aria-hidden="true">
        <circle cx="12" cy="12" r="10"/>
        <ellipse cx="12" cy="12" rx="4.5" ry="10"/>
        <line x1="2" y1="12" x2="22" y2="12"/>
        <path d="M4 7h16M4 17h16"/>
      </svg>
      <span>@voteformarty.net</span>
    </div>
  </div>
</div>
</body>
</html>
```